I will be video blogging 1 - 5 minute instructional videos about all kind or stuff

I want it took look clean.
I have secured Marcusdellorn.com
Do you design vidnexa pages as well.
I will upload to vidnexa and correspond with websites.
Website wil include
videos with longer written description
how to book me.
where I am speaking at next
Thank you

Reason: my design is going to be more detailed than i had expected

Reason: still have changes

Vidnexa

```html
<!DOCTYPE html>
<html lang="en">
<head>
<meta charset="utf-8">
<title>MarcusDellorn.com</title>
<link href="https://fonts.googleapis.com/css2?family=Open+Sans:wght@400;600;700&display=swap" rel="stylesheet">
<style>
  :root {
    --page: #ffffff;
    --wood-top: #4e2b06;
    --wood-mid: #3a2006;
    --wood-bottom: #2c1a06;
    --accent: #00aeef;
    --accent-light: #2fc0f5;
    --teal: #3fc4da;
    --ink: #111111;
    --panel: #efefef;
    --divider: #b9b9b9;
    --tab: #1c1c1c;
    --tab-fold: #000000;
    --video: #1f1d1a;
    --controls: #0d0d0d;
  }
  * { box-sizing: border-box; margin: 0; padding: 0; }
  html, body { width: 1200px; height: 1000px; overflow: hidden; background: var(--page); }
  body { position: relative; font-family: "Open Sans", Arial, sans-serif; color: var(--ink); }

  .backdrop {
    position: absolute; left: 248px; top: 8px; width: 694px; height: 984px;
    background: linear-gradient(180deg, var(--wood-top) 0%, var(--wood-mid) 30%, var(--wood-bottom) 100%);
  }
  .brand {
    position: absolute; left: 372px; top: 31px; display: flex; align-items: center; gap: 6px;
    color: #fff; font-weight: 700; font-size: 17.5px; letter-spacing: 0;
  }
  .brand-dot { width: 11px; height: 11px; border-radius: 50%; background: var(--accent); }

  .site-nav {
    position: absolute; left: 364px; top: 66px; width: 462px; height: 26px;
    background: linear-gradient(180deg, var(--accent-light), var(--accent));
  }
  .site-nav ul { list-style: none; display: flex; gap: 11px; padding-left: 6px; height: 100%; align-items: center; }
  .site-nav li { color: #fff; font-size: 7.5px; font-weight: 600; }
  .nav-pointer { position: absolute; left: 369px; top: 92px; }
  .search {
    position: absolute; left: 673px; top: 70px; width: 105px; height: 18px;
    background: #fff; border: 1px solid #7fd6f7; border-radius: 2px; display: flex;
  }
  .search span { flex: 1; font-size: 6.5px; color: #aaa; padding: 4px 5px; }
  .search i { width: 20px; border-left: 1px solid #ccc; display: flex; align-items: center; justify-content: center; }
  .social { position: absolute; top: 72px; width: 14px; height: 14px; border-radius: 50%; border: 1.5px solid #fff; background: #3a8fd4; }

  .content { position: absolute; left: 364px; top: 92px; width: 462px; height: 893px; background: var(--page); }

  .post-title-tab { position: absolute; left: 352px; width: 38px; height: 27px; background: var(--tab); }
  .post-title-tab::before {
    content: ""; position: absolute; left: 11px; top: 3px; width: 20px; height: 20px;
    border-radius: 50%; background: var(--teal);
  }
  .post-title-tab svg { position: absolute; left: 17px; top: 8px; }
  .post-title-tab::after {
    content: ""; position: absolute; left: 0; top: 27px;
    border-top: 6px solid var(--tab-fold); border-left: 12px solid transparent;
  }
  .post-title { position: absolute; left: 396px; font-size: 15px; font-weight: 400; line-height: 20px; letter-spacing: -0.2px; white-space: nowrap; }

  .video {
    position: absolute; left: 384px; width: 261px; height: 163px;
    border: 3px solid var(--accent); border-radius: 3px; overflow: hidden; background: var(--video);
  }
  .video-still { position: absolute; inset: 0 0 12px 0; }
  .video-controls { position: absolute; left: 0; right: 0; bottom: 0; height: 12px; background: var(--controls); }
  .play-now {
    position: absolute; left: 50%; top: 50%; transform: translate(-50%, -58%);
    display: flex; align-items: center; gap: 5px; color: #fff; font-size: 10.5px; white-space: nowrap;
  }
  .play-icon { width: 21px; height: 21px; border: 2px solid #fff; border-radius: 50%; position: relative; }
  .play-icon::after {
    content: ""; position: absolute; left: 6px; top: 4.5px;
    border-left: 6px solid #fff; border-top: 4px solid transparent; border-bottom: 4px solid transparent;
  }

  .widget-head {
    position: absolute; left: 684px; width: 135px; height: 20px; background: var(--accent);
    color: #fff; font-size: 7.5px; font-weight: 600; text-align: center; line-height: 20px;
  }
  .widget-body { position: absolute; left: 684px; width: 135px; background: var(--panel); }
  .widget-divider { position: absolute; left: 684px; width: 135px; height: 4px; background: var(--divider); }

  .mini-video { position: absolute; left: 687px; width: 64px; height: 38px; border: 2px solid var(--accent); background: var(--video); }
  .mini-video .play-now { font-size: 5.5px; gap: 3px; transform: translate(-50%, -50%); }
  .mini-video .play-icon { width: 11px; height: 11px; border-width: 1.5px; }
  .mini-video .play-icon::after { left: 3px; top: 2px; border-left-width: 3.5px; border-top-width: 2.5px; border-bottom-width: 2.5px; }
  .mini-duration { position: absolute; right: 2px; bottom: 0; font-size: 5px; color: #ddd; }
  .mini-title { position: absolute; left: 754px; width: 66px; font-size: 8.8px; line-height: 10px; color: var(--ink); letter-spacing: -0.1px; }
</style>
</head>
<body>
  <div class="backdrop"></div>

  <div class="brand"><span>MARCUSDELLORN.COM</span><span class="brand-dot"></span></div>

  <nav class="site-nav">
    <ul><li>Home</li><li>Videos</li><li>Discussion</li><li>About</li></ul>
  </nav>
  <svg class="nav-pointer" width="10" height="6" viewBox="0 0 10 6"><path d="M0 0 H10 L5 6 Z" fill="#00aeef"/></svg>
  <div class="search"><span>search</span><i><svg width="10" height="10" viewBox="0 0 10 10"><circle cx="4" cy="4" r="3" fill="none" stroke="#333" stroke-width="1.3"/><path d="M6 6 L9.5 9.5" stroke="#333" stroke-width="1.6"/></svg></i></div>
  <div class="social" style="left:785px"></div>
  <div class="social" style="left:804px"></div>

  <main class="content"></main>

  <div class="post-title-tab" style="top:115px"><svg width="9" height="10" viewBox="0 0 9 10"><path d="M0 0 L9 5 L0 10 Z" fill="#fff"/></svg></div>
  <h2 class="post-title" style="top:116px">How to make a wood clock</h2>
  <div class="video" style="top:152px">
    <div class="video-still" role="img" aria-label="Video still of hands marking a wooden board on a workbench" style="background:radial-gradient(ellipse at 50% 45%, #3a342a, #171512 75%)"></div>
    <div class="video-controls"></div>
    <div class="play-now"><span class="play-icon"></span>PLAY NOW!</div>
  </div>

  <div class="post-title-tab" style="top:326px"><svg width="9" height="10" viewBox="0 0 9 10"><path d="M0 0 L9 5 L0 10 Z" fill="#fff"/></svg></div>
  <h2 class="post-title" style="top:327px">How to make a headboard</h2>
  <div class="video" style="top:364px">
    <div class="video-still" role="img" aria-label="Video still of a miter saw cutting a board" style="background:radial-gradient(ellipse at 45% 50%, #34342e, #141412 75%)"></div>
    <div class="video-controls"></div>
    <div class="play-now"><span class="play-icon"></span>PLAY NOW!</div>
  </div>

  <div class="post-title-tab" style="top:539px"><svg width="9" height="10" viewBox="0 0 9 10"><path d="M0 0 L9 5 L0 10 Z" fill="#fff"/></svg></div>
  <h2 class="post-title" style="top:544px">How to make a longboard</h2>
  <div class="video" style="top:580px">
    <div class="video-still" role="img" aria-label="Video still of a table saw ripping a wooden plank outdoors" style="background:linear-gradient(160deg, #3e362c, #2a2520 55%, #3a1c18)"></div>
    <div class="video-controls"></div>
    <div class="play-now"><span class="play-icon"></span>PLAY NOW!</div>
  </div>

  <div class="post-title-tab" style="top:753px"><svg width="9" height="10" viewBox="0 0 9 10"><path d="M0 0 L9 5 L0 10 Z" fill="#fff"/></svg></div>
  <h2 class="post-title" style="top:758px">How to make a longboard</h2>
  <div class="video" style="top:794px">
    <div class="video-still" role="img" aria-label="Video still of a table saw ripping a wooden plank outdoors" style="background:linear-gradient(160deg, #3e362c, #2a2520 55%, #3a1c18)"></div>
    <div class="video-controls"></div>
    <div class="play-now"><span class="play-icon"></span>PLAY NOW!</div>
  </div>

  <div class="widget-head" style="top:111px">RECENT VIDEOS</div>
  <div class="widget-body" style="top:131px; height:144px"></div>
  <div class="mini-video" style="top:140px" role="img" aria-label="Thumbnail for video 1"><div class="play-now"><span class="play-icon"></span>PLAY NOW!</div><span class="mini-duration">7:18</span></div>
  <p class="mini-title" style="top:141px">How to make a video 1</p>
  <div class="mini-video" style="top:184px" role="img" aria-label="Thumbnail for video 2"><div class="play-now"><span class="play-icon"></span>PLAY NOW!</div><span class="mini-duration">5:20</span></div>
  <p class="mini-title" style="top:185px">How to make a video 2</p>
  <div class="mini-video" style="top:230px" role="img" aria-label="Thumbnail for video 3"><div class="play-now"><span class="play-icon"></span>PLAY NOW!</div><span class="mini-duration">6:08</span></div>
  <p class="mini-title" style="top:232px">How to make a video 3</p>

  <div class="widget-divider" style="top:286px"></div>
  <div class="widget-head" style="top:299px">LATEST TWEETS</div>
  <div class="widget-body" style="top:319px; height:144px"></div>

  <div class="widget-divider" style="top:473px"></div>
  <div class="widget-head" style="top:487px">LATEST POST</div>
  <div class="widget-body" style="top:507px; height:145px"></div>
</body>
</html>
```